Erklär-Flyer für Gutschein-Ankauf-Service Bonkarten-Profi.de
Zielgruppe
Auf http://www.bonkarten-profi.de/ bieten wir u.a. den Service an, ungenutzte Geschenkkarten von großen Händlern wie z.B. Technoplatz, Vandoro, WOLM, usw. direkt gegen Bargeld einzutauschen. Diesen Service wollen wir nun in einem Flyer vorstellen.
Die Zielgruppe des zu erstellenden Flyers sollen vor allem Mitarbeiter bei Firmen z.B. Auto Verkäufer sein, die von Ihrem Arbeitgeber als Prämie Geschenkgutscheine als Incentive erhalten und diese aber lieber in Bargeld umtauschen würden.
Das Wunschszenario wäre: Wir schicken den Flyer zusammen mit einem Anschreiben an die jeweiligen Firmen. Der/diejenige die den Brief und Flyer entgegennimmt, erkennt den Sinn und Nutzen und gibt den Flyer an Ihre Kollegen weiter bzw. hängt ihn ans schwarze Brett etc.
Aufgabenstellung
Gestaltet werden soll ein 3 Schritte Falz-Flyer (z.B. 6-seitiger Altarfalz Fensterfalz) angelehnt an das bisherige Design auf Bonkarten-Profi.de (nicht zwingend 100%, gerne auch eigene Ideen). Auf der Außenseite nur kurz in einem Satz um was es geht und auf der Innenseite dann am Besten in 3 Schritten erklärt, wie einfach der Umtausch von Gutscheinen in Bargeld ist.
Das Wichtigste ist die "Bequemlichkeit, Einfachheit, kein Aufwand", am zweitwichtigsten ist "Sicherheit, Seriosität" (Unsere Seite gibt es schon seit 2008 und wir wurden bereits im KRT vorgestellt).
Verteilung des Falt-Flyer als Brief mit der Post. Wenn der Brief geöffnet wird ist der zu erreichende Optimal Zustand, dass der Flyer von der Person, die den Brief öffnet, z.B. ans "schwarze Brett" gehängt wird als Info bzw. eine Art Anleitung.

```html
<!DOCTYPE html>
<html lang="de">
<head>
<meta charset="utf-8">
<title>Bonkarten-Profi.de – Falzflyer</title>
<link rel="stylesheet" href="https://fonts.googleapis.com/css2?family=Ubuntu:wght@400;500&display=swap">
<style>
  :root{
    --green:#8bb828;
    --green-dark:#6f9a1a;
    --blue:#1a6aa8;
    --orange:#ee7a12;
    --ink:#3c3c3c;
    --grey-bg:#e9eaeb;
    --white:#ffffff;
  }
  *{margin:0;padding:0;box-sizing:border-box}
  html,body{width:1200px;height:840px;overflow:hidden;background:var(--white)}
  body{position:relative;font-family:"Ubuntu",sans-serif;color:var(--ink)}
  .sheet{position:absolute;left:73px;width:1062px;height:355px;background:var(--grey-bg);overflow:hidden;box-shadow:0 0 3px rgba(0,0,0,.15)}
  .sheet--outer{top:51px;background:linear-gradient(180deg,#f1f1f1,#e3e4e5)}
  .sheet--inner{top:450px}
  .fold{position:absolute;top:0;bottom:0;border-left:1px dashed #b9bcbf}
  .abs{position:absolute}
  .photo{position:absolute}
  .lead{background:var(--green);color:var(--white);font-size:12.5px;line-height:18px;padding:8px 10px;border-radius:2px}
  .textbox{background:var(--white);border:1.5px solid var(--green);border-radius:3px;padding:6px 10px;font-size:9.6px;line-height:15.2px}
  .url{font-size:10px;font-weight:500;color:#555;text-align:right}
  .brand{color:var(--green-dark);font-weight:500;font-size:20px;line-height:21px;text-align:right}
  .brand span{display:block}
  .social{font-size:7.6px;line-height:12px;color:#444}
  .social-icon{width:26px;height:26px;border-radius:4px;background:#3f90cf;display:inline-block;margin-right:4px}
  .review{width:120px;height:94px}
  .review svg.bubble{position:absolute;left:0;top:0}
  .review-body{position:absolute;left:2px;top:0;width:116px;text-align:center;color:var(--white)}
  .review-title{margin-top:10px;font-size:8.4px;line-height:11px;font-weight:500}
  .review-stars{display:flex;justify-content:center;gap:3px;margin-top:5px;height:14px}
  .review-text{margin-top:5px;font-size:6.6px;line-height:9px}
  .review-source{margin-top:3px;font-size:7px;line-height:9px}
  .claim{background:var(--blue);color:var(--white);font-size:15.5px;line-height:22px;padding:10px 14px;border-radius:3px}
  .benefits{background:var(--green);color:var(--white);font-size:15.5px;line-height:22px;padding:9px 10px;border-radius:3px;list-style:none}
  .benefits li{display:flex;align-items:center;gap:8px}
  .known{border-radius:50%;background:var(--orange);box-shadow:0 0 0 5px rgba(255,255,255,.75);color:var(--white);text-align:center;font-weight:500}
  .step-band{position:absolute;left:0;right:0;top:0;height:74px;background:linear-gradient(180deg,#dcdedf,#eeeff0)}
  .step-num,.step-title{position:absolute;top:23px;height:32px;background:var(--green);color:var(--white);font-size:19px;line-height:32px;font-weight:500;border-radius:2px;text-align:center;box-shadow:0 0 0 2px rgba(255,255,255,.7)}
  .step-strip{position:absolute;top:74px;height:171px;background:var(--white)}
  .zoom{position:absolute;border-radius:50%;border:2px solid var(--green);box-shadow:0 0 0 2px var(--white)}
  .step-text{position:absolute;top:262px;height:47px;background:var(--white);border:1.5px solid var(--green);border-radius:3px;padding:5px 10px;font-size:12.4px;line-height:18px}
</style>
</head>
<body>

<section class="sheet sheet--outer" aria-label="Außenseite">
  <div class="photo" role="img" aria-label="Foto: Stapel bunter Geschenkkarten" style="left:0;top:0;width:620px;height:175px;background:linear-gradient(90deg,rgba(214,70,60,.55),rgba(240,200,60,.5) 25%,rgba(90,160,210,.5) 45%,rgba(190,190,190,.3) 70%,rgba(233,234,235,0)),linear-gradient(180deg,rgba(255,255,255,0),rgba(233,234,235,1) 98%)"></div>
  <div class="fold" style="left:354px"></div>
  <div class="fold" style="left:706px"></div>

  <p class="lead abs" style="left:22px;top:123px;width:309px">Sie haben uneingelößte Gutscheine herumliegen?<br>Machen Sie diese bequem und sicher zu Bargeld!</p>
  <p class="textbox abs" style="left:22px;top:186px;width:309px">Wir kaufen nicht benötigte Wertgutscheine / Geschenkgutscheine. Im Gegensatz zu Foren, Tauschportalen oder Auktionen werden Sie Ihren nicht benötigten Gutschein bei uns sofort los und bekommen das Geld direkt auf Ihr Konto. Der Vorteil: Bei uns sehen Sie sofort wie viel Sie für Ihren Gutschein bekommen. Ohne Umwege und ohne Risiko. Und das Ganze in nur drei einfachen Schritten ...</p>
  <p class="url abs" style="left:180px;top:325px;width:151px">bonkarten-profi.de</p>

  <div class="brand abs" style="left:560px;top:28px;width:132px"><span>Bonkarten</span><span>Profi</span></div>
  <div class="review abs" style="left:566px;top:224px">
    <svg class="bubble" width="120" height="94" viewBox="0 0 120 94" aria-hidden="true">
      <path d="M4 2h112a3 3 0 0 1 3 3v71a3 3 0 0 1-3 3H86l-10 12-8-12H4a3 3 0 0 1-3-3V5a3 3 0 0 1 3-3z" fill="var(--green)" stroke="#fff" stroke-width="2"/>
    </svg>
    <div class="review-body">
      <p class="review-title">Unsere Kunden lieben uns!</p>
      <div class="review-stars" aria-label="4 Sterne">
        <svg width="14" height="14" viewBox="0 0 24 24" aria-hidden="true"><path d="M12 1.5l3.1 7.1 7.7.7-5.8 5.1 1.7 7.6L12 18l-6.7 4 1.7-7.6-5.8-5.1 7.7-.7z" fill="#fff"/></svg>
        <svg width="14" height="14" viewBox="0 0 24 24" aria-hidden="true"><path d="M12 1.5l3.1 7.1 7.7.7-5.8 5.1 1.7 7.6L12 18l-6.7 4 1.7-7.6-5.8-5.1 7.7-.7z" fill="#fff"/></svg>
        <svg width="14" height="14" viewBox="0 0 24 24" aria-hidden="true"><path d="M12 1.5l3.1 7.1 7.7.7-5.8 5.1 1.7 7.6L12 18l-6.7 4 1.7-7.6-5.8-5.1 7.7-.7z" fill="#fff"/></svg>
        <svg width="14" height="14" viewBox="0 0 24 24" aria-hidden="true"><path d="M12 1.5l3.1 7.1 7.7.7-5.8 5.1 1.7 7.6L12 18l-6.7 4 1.7-7.6-5.8-5.1 7.7-.7z" fill="#fff"/></svg>
      </div>
      <p class="review-text">Wir haben bereits sehr viele<br>positive Kundenbewertungen</p>
      <p class="review-source">Kundenstimme</p>
    </div>
  </div>
  <div class="abs" style="left:375px;top:308px;display:flex;align-items:center">
    <span class="social-icon"></span><span class="social-icon" style="background:#3b5a9a"></span>
    <p class="social" style="margin-left:4px">Folge uns auf Piepnetz und<br>werde unser Fan auf Freundbuch!</p>
  </div>
  <p class="url abs" style="left:560px;top:325px;width:132px">bonkarten-profi.de</p>

  <div class="photo" role="img" aria-label="Foto: lächelnde Frau mit Einkaufstaschen hält eine Geschenkkarte" style="left:707px;top:0;width:355px;height:355px;background:linear-gradient(160deg,#c9a27e 0%,#e8d9c4 35%,#d7dde0 65%,#eceeef 100%)"></div>
  <div class="brand abs" style="left:920px;top:28px;width:122px"><span>Bonkarten</span><span>Profi</span></div>
  <div class="known abs" style="left:928px;top:120px;width:88px;height:88px;padding-top:18px;font-size:13px;line-height:15px">Bekannt<br>aus dem<br><span style="font-size:20px;line-height:24px">KRT</span></div>
  <p class="claim abs" style="left:729px;top:226px;width:189px">Wir machen Ihre ungenutzen Gutscheine zu Bargeld!</p>
  <ul class="benefits abs" style="left:929px;top:226px;width:112px;height:84px">
    <li><svg width="13" height="13" viewBox="0 0 14 14" aria-hidden="true"><circle cx="7" cy="7" r="7" fill="#fff"/><path d="M3.5 7.2l2.3 2.3 4.7-4.7" fill="none" stroke="var(--green)" stroke-width="2"/></svg>Bequem</li>
    <li><svg width="13" height="13" viewBox="0 0 14 14" aria-hidden="true"><circle cx="7" cy="7" r="7" fill="#fff"/><path d="M3.5 7.2l2.3 2.3 4.7-4.7" fill="none" stroke="var(--green)" stroke-width="2"/></svg>Einfach</li>
    <li><svg width="13" height="13" viewBox="0 0 14 14" aria-hidden="true"><circle cx="7" cy="7" r="7" fill="#fff"/><path d="M3.5 7.2l2.3 2.3 4.7-4.7" fill="none" stroke="var(--green)" stroke-width="2"/></svg>Sicher</li>
  </ul>
  <p class="url abs" style="left:920px;top:325px;width:122px">bonkarten-profi.de</p>
</section>

<section class="sheet sheet--inner" aria-label="Innenseite">
  <div class="step-band"></div>
  <div class="fold" style="left:354px"></div>
  <div class="fold" style="left:706px"></div>

  <div class="step-num" style="left:22px;width:32px">1</div>
  <div class="step-title" style="left:61px;width:158px">Anbieter wählen</div>
  <div class="step-strip photo" role="img" aria-label="Foto: junge Frau am Laptop auf der Webseite" style="left:0;width:354px;background:linear-gradient(90deg,#b98a6c,#d8c2ae 40%,#5d7fa8 60%,#cfd8e2)"></div>
  <div class="zoom photo" role="img" aria-label="Vergrößerter Ausschnitt der Webseite: Anbieter auswählen" style="left:201px;top:86px;width:144px;height:144px;background:radial-gradient(circle,#ffffff 40%,#e6eef5)"></div>
  <p class="step-text" style="left:22px;width:312px">Gehen Sie auf www.bonkarten-profi.de und wählen Sie Ihren Geschenkanbieter aus.</p>
  <p class="url abs" style="left:180px;top:322px;width:151px">bonkarten-profi.de</p>

  <div class="step-num" style="left:377px;width:32px">2</div>
  <div class="step-title" style="left:415px;width:159px">Daten eingeben</div>
  <div class="step-strip photo" role="img" aria-label="Foto: Laptop mit geöffneter Webseite" style="left:355px;width:351px;background:linear-gradient(180deg,#cfd9e4,#f2f4f6 55%,#2a2a2a 80%,#444)"></div>
  <div class="zoom photo" role="img" aria-label="Vergrößerter Ausschnitt der Webseite: Gutscheine eingeben" style="left:556px;top:86px;width:144px;height:144px;background:radial-gradient(circle,#ffffff 40%,#e6eef5)"></div>
  <p class="step-text" style="left:377px;width:312px">Melden Sie sich kostenlos an und geben Sie Ihre Gutschein-Informationen ein.</p>
  <p class="url abs" style="left:560px;top:322px;width:132px">bonkarten-profi.de</p>

  <div class="step-num" style="left:731px;width:32px">3</div>
  <div class="step-title" style="left:769px;width:159px">Geld aufs Konto</div>
  <div class="step-strip photo" role="img" aria-label="Foto: jubelnde Frau mit Geldscheinen" style="left:707px;width:355px;background:linear-gradient(90deg,#f4f4f4,#b98064 20%,#e8d3bf 35%,#f2f2f2 55%)"></div>
  <div class="zoom photo" role="img" aria-label="Foto: Umschlag wird in einen gelben Briefkasten gesteckt" style="left:903px;top:86px;width:144px;height:144px;background:radial-gradient(circle at 55% 45%,#d9b78a,#e2b93a 55%,#b8922a)"></div>
  <p class="step-text" style="left:731px;width:312px;font-size:12px">Ausdrucken und den Gutschein direkt an uns senden. Das Geld erhalten Sie direkt auf Ihr Konto.</p>
  <p class="url abs" style="left:920px;top:322px;width:122px">bonkarten-profi.de</p>
</section>

</body>
</html>
```